■依頼の目的/概要

当社は、宮城県仙台市にて、新築・リフォーム事業を行っている会社です。
女性に好まれるようなサイトデザインにしたく、今回、制作依頼致します。

■ホームページ内容

TOPページ / リフォーム事例 / お問合せ 合計3ページ

■重視する点/検討基準

・女性(主婦)に好まれるようなデザイン
・リフォームを相談したくなる
・楽しそうな夢を叶えてくれそうな…
・素人目線でのアイディア・ご提案コンテンツがあれば尚可

■ご質問

その他、疑問点がありましたら、お気軽にご質問ください。
株式会社 みのり舎 http://www.minori-sha.co.jp/
デザイナーさんの能力を十分に発揮して頂きたいので、
納品ファイル形式は、限定しておりませんでしたが、
好ましい形式を記載致します。

html、css、それに関連する画像ファイル。
Flash 、JavaScriptなども使用可。
フォトショップ形式、イラストレーター形式。
コーディング無しの全3ページのサイトデザイン。

マル写真と家のイラストで、やわらかいイメージを与える。
トップページを見ただけで、会社の特徴がわかる。

この度は、皆様に多くのご提案して頂きまして、誠にありがとうございました。それぞれのご提案に良い点があり、一人の方に選択するのが、難航をし、また、大変心苦しかったです。
また、何かありましたら、ご提案して頂けましたら幸いです。
今後とも、何卒、よろしくお願い致します。

```html
<!DOCTYPE html>
<html lang="ja">
<head>
<meta charset="UTF-8">
<title>株式会社 みのり舎</title>
<link rel="stylesheet" href="https://fonts.googleapis.com/css2?family=Noto+Sans+JP:wght@400;700&family=Noto+Serif+JP:wght@400;700&family=Oswald:wght@500&display=swap">
<style>
:root{
  --pink:#e8727a;
  --pink-soft:#f6c9cc;
  --pink-pale:#fdf0f0;
  --red:#c9383f;
  --ink:#4a4340;
  --ink-soft:#8a817c;
  --line:#e6dedb;
  --paper:#ffffff;
  --wall:#f3ebe2;
}
*{margin:0;padding:0;box-sizing:border-box}
html,body{width:828px;height:1200px;overflow:hidden;background:var(--paper)}
body{font-family:"Noto Sans JP",sans-serif;color:var(--ink);position:relative}
.page{position:relative;width:828px;height:1200px}

/* header */
.site-header{position:absolute;left:69px;top:18px;width:690px;height:80px}
.brand{position:absolute;left:0;top:4px}
.brand-row{display:flex;align-items:center;gap:8px}
.brand-mark{width:18px;height:18px;background:var(--pink)}
.brand-name{font-size:19px;font-weight:700;color:var(--ink);letter-spacing:2px}
.brand-url{font-size:9px;color:var(--ink-soft);margin-top:4px;margin-left:26px}
.brand-tag{font-size:10px;color:var(--pink);margin-top:3px;margin-left:26px;letter-spacing:1px}
.header-actions{position:absolute;right:0;top:4px;display:flex;gap:8px}
.btn-head{background:var(--pink);color:#fff;font-size:11px;font-weight:700;height:24px;padding:0 16px;display:flex;align-items:center;gap:6px;border-radius:2px}
.btn-head svg{width:12px;height:12px}

/* nav */
.global-nav{position:absolute;left:69px;top:106px;width:690px;display:flex;justify-content:space-between;border-bottom:1px solid var(--line);padding-bottom:8px}
.nav-item{text-align:center}
.nav-en{display:block;font-family:"Oswald",sans-serif;font-size:15px;font-weight:500;letter-spacing:1px;color:var(--ink)}
.nav-jp{display:block;font-size:8px;color:var(--ink-soft);margin-top:1px}
.nav-item.is-current .nav-en{color:var(--pink)}

/* hero */
.hero{position:absolute;left:69px;top:160px;width:690px;height:460px;overflow:hidden;background:var(--wall)}
.hero-photo{position:absolute;left:0;top:0;width:490px;height:460px;background:linear-gradient(160deg,#e9d9c2 0%,#c9a57c 45%,#8a6040 80%,#5b3e29 100%)}
.hero-wall{position:absolute;left:490px;top:0;width:200px;height:460px;background:linear-gradient(180deg,#f7f1ea,#ece1d4)}
.hero-small,.hero-title,.hero-sub{position:absolute;writing-mode:vertical-rl;font-family:"Noto Serif JP",serif;white-space:nowrap}
.hero-small{right:16px;top:22px;font-size:11px;line-height:1.5;letter-spacing:2px;color:var(--ink)}
.hero-title{right:62px;top:30px;font-size:30px;font-weight:700;color:var(--red);letter-spacing:6px;line-height:1}
.hero-sub{right:110px;top:44px;font-size:13px;line-height:1.6;letter-spacing:3px;color:var(--ink)}
.hero-badge{position:absolute;right:40px;bottom:26px;width:78px;height:78px;border-radius:50%;background:var(--pink);color:#fff;font-size:10px;font-weight:700;text-align:center;display:flex;flex-direction:column;justify-content:center;line-height:1.4}
.hero-dots{position:absolute;left:0;right:0;top:626px;display:flex;justify-content:center;gap:6px}
.hero-dots span{width:6px;height:6px;border-radius:50%;background:var(--pink-soft)}
.hero-dots span.on{background:var(--pink)}

/* features */
.features{position:absolute;left:69px;top:648px;width:690px;display:flex;justify-content:space-between}
.feature{width:166px}
.feature-head{display:flex;align-items:center;gap:6px;height:34px;border-bottom:2px solid var(--pink-soft)}
.feature-icon{width:20px;height:20px;border-radius:50%;background:var(--pink);flex:none;display:flex;align-items:center;justify-content:center}
.feature-icon svg{width:12px;height:12px}
.feature-title{font-size:13px;font-weight:700}
.feature-en{display:block;font-size:7px;color:var(--ink-soft);font-weight:400}
.feature-photo{margin-top:8px;width:166px;height:128px}
.photo-health{background:linear-gradient(150deg,#d9c3a4,#9b7652)}
.photo-wood{background:linear-gradient(150deg,#b9c7a4,#6f7d55)}
.photo-stone{background:linear-gradient(150deg,#d7d0c4,#9c9284)}
.photo-craft{background:linear-gradient(150deg,#e2d2bc,#a98563)}

/* about */
.about{position:absolute;left:69px;top:850px;width:690px;height:250px;border-top:1px solid var(--line);padding-top:28px}
.about-circle{position:absolute;left:8px;top:30px;width:150px;height:150px;border-radius:50%;border:6px solid var(--pink-soft);display:flex;align-items:center;justify-content:center}
.about-circle-inner{width:122px;height:122px;border-radius:50%;background:var(--pink);color:#fff;font-family:"Noto Serif JP",serif;font-size:26px;font-weight:700;line-height:1.2;text-align:center;display:flex;align-items:center;justify-content:center;letter-spacing:2px}
.about-body{position:absolute;left:190px;top:30px;width:500px}
.about-title{font-size:18px;font-weight:700;color:var(--pink);letter-spacing:1px}
.about-lead{font-size:10px;color:var(--ink);margin-top:4px}
.about-text{font-size:9.5px;line-height:1.8;color:var(--ink-soft);margin-top:14px}
.about-links{display:flex;gap:10px;margin-top:18px}
.about-link{flex:1;height:30px;background:var(--pink);color:#fff;font-size:10px;font-weight:700;display:flex;align-items:center;justify-content:center;gap:4px;border-radius:2px}

/* footer */
.to-top{position:absolute;right:69px;top:1100px;width:32px;height:32px;border-radius:50%;background:var(--pink);color:#fff;font-family:"Oswald",sans-serif;font-size:10px;display:flex;align-items:center;justify-content:center}
.site-footer{position:absolute;left:69px;top:1120px;width:690px;border-top:3px solid var(--pink-soft);padding-top:14px;display:flex;justify-content:space-between}
.footer-info{font-size:9px;line-height:1.6;color:var(--ink-soft)}
.footer-info strong{display:block;font-size:11px;color:var(--ink)}
.footer-links{font-size:9px;color:var(--ink-soft);text-align:right;line-height:1.8}
</style>
</head>
<body>
<div class="page">

  <header class="site-header">
    <div class="brand">
      <div class="brand-row"><span class="brand-mark"></span><span class="brand-name">みのり舎</span></div>
      <div class="brand-url">http://www.minori-sha.co.jp/</div>
      <div class="brand-tag">家族の笑顔をかたちにします</div>
    </div>
    <div class="header-actions">
      <div class="btn-head">
        <svg viewBox="0 0 24 24"><path fill="#fff" d="M6.6 10.8a15 15 0 0 0 6.6 6.6l2.2-2.2c.3-.3.7-.4 1-.2 1.1.4 2.3.6 3.6.6.6 0 1 .4 1 1V20c0 .6-.4 1-1 1A17 17 0 0 1 3 4c0-.6.4-1 1-1h3.5c.6 0 1 .4 1 1 0 1.3.2 2.5.6 3.6.1.3 0 .7-.2 1z"/></svg>
        0120-000-123
      </div>
      <div class="btn-head">ご相談窓口</div>
    </div>
  </header>

  <nav class="global-nav">
    <div class="nav-item is-current"><span class="nav-en">HOME</span><span class="nav-jp">トップ</span></div>
    <div class="nav-item"><span class="nav-en">PRICE</span><span class="nav-jp">価格表</span></div>
    <div class="nav-item"><span class="nav-en">VOICE</span><span class="nav-jp">お客様の声</span></div>
    <div class="nav-item"><span class="nav-en">STAFF</span><span class="nav-jp">スタッフ</span></div>
    <div class="nav-item"><span class="nav-en">WINNING</span><span class="nav-jp">受賞歴</span></div>
    <div class="nav-item"><span class="nav-en">WORK</span><span class="nav-jp">施工事例</span></div>
    <div class="nav-item"><span class="nav-en">IDEA</span><span class="nav-jp">リフォームアイデア</span></div>
    <div class="nav-item"><span class="nav-en">FURNITURE</span><span class="nav-jp">オリジナル家具</span></div>
  </nav>

  <section class="hero">
    <div class="hero-photo" role="img" aria-label="明るい木のリビングに照明とテレビ台のある施工事例の写真"></div>
    <div class="hero-wall"></div>
    <p class="hero-small">二〇一三年 第十五回<br>全国すまいデザインコンテスト</p>
    <p class="hero-title">全国優秀賞受賞</p>
    <p class="hero-sub">木のぬくもりと暮らしやすさ<br>を追求したリビング改装</p>
    <div class="hero-badge">2013年<br>みのり舎<br>施工事例</div>
  </section>
  <div class="hero-dots"><span class="on"></span><span></span><span></span><span></span></div>

  <section class="features">
    <article class="feature">
      <div class="feature-head"><span class="feature-icon"><svg viewBox="0 0 24 24"><path fill="#fff" d="M12 3 2 12h3v8h5v-5h4v5h5v-8h3z"/></svg></span><span class="feature-title">健康住宅<span class="feature-en">Healthy House</span></span></div>
      <div class="feature-photo photo-health" role="img" aria-label="自然素材を使った明るい室内の写真"></div>
    </article>
    <article class="feature">
      <div class="feature-head"><span class="feature-icon"><svg viewBox="0 0 24 24"><path fill="#fff" d="M12 3 2 12h3v8h5v-5h4v5h5v-8h3z"/></svg></span><span class="feature-title">厳選木材<span class="feature-en">Wood</span></span></div>
      <div class="feature-photo photo-wood" role="img" aria-label="木材を手に持つ職人の写真"></div>
    </article>
    <article class="feature">
      <div class="feature-head"><span class="feature-icon"><svg viewBox="0 0 24 24"><path fill="#fff" d="M12 3 2 12h3v8h5v-5h4v5h5v-8h3z"/></svg></span><span class="feature-title">天然石・タイル<span class="feature-en">Stone &amp; Tile</span></span></div>
      <div class="feature-photo photo-stone" role="img" aria-label="天然石の床とタイルの写真"></div>
    </article>
    <article class="feature">
      <div class="feature-head"><span class="feature-icon"><svg viewBox="0 0 24 24"><path fill="#fff" d="M12 3 2 12h3v8h5v-5h4v5h5v-8h3z"/></svg></span><span class="feature-title">自社職人<span class="feature-en">Craftsman</span></span></div>
      <div class="feature-photo photo-craft" role="img" aria-label="作業中の自社職人の写真"></div>
    </article>
  </section>

  <section class="about">
    <div class="about-circle"><div class="about-circle-inner">一貫<br>体制</div></div>
    <div class="about-body">
      <h2 class="about-title">みのり舎とは？</h2>
      <p class="about-lead">設計から施工・アフターまで自社で一貫して行う住まいの工房です</p>
      <p class="about-text">みのり舎は、ご相談からプランニング、デザイン、施工、アフターメンテナンスまでを自社スタッフと自社職人で一貫して担当します。窓口がひとつなので想いが伝わりやすく、ご家族の暮らしに寄り添った住まいづくりをお届けします。</p>
      <div class="about-links">
        <div class="about-link">▶ 施工事例を見る</div>
        <div class="about-link">▶ お客様の声を見る</div>
        <div class="about-link">▶ 無料相談・お問い合わせ</div>
      </div>
    </div>
  </section>

  <div class="to-top">TOP</div>
  <footer class="site-footer">
    <div class="footer-info">
      <strong>株式会社 みのり舎</strong>
      宮城県みのり市中央1丁目2-3<br>
      TEL 0120-000-123 / FAX 022-000-0000
    </div>
    <div class="footer-links">
      トップページ ｜ 施工事例 ｜ お問い合わせ<br>
      プライバシーポリシー ｜ サイトマップ
    </div>
  </footer>

</div>
</body>
</html>
```